TWL Business Card Design Project

Real Estate Broker, Realtor
I would like something similar to what I have attached from Corvell Realty except my company is Marlow Realty Group, LLC. Instead of a single "M" on the back I would like "TWL". Phone # 816-552-4917
Name - Dorian Faulk
Licensed in the State of Missouri
No address
email - dfaulk@marlowhomesexample.com
Contact Information for Business Card
I would like something similar to what I have attached from Corvell Realty except my company is Marlow Realty Group, LLC. Instead of a single "M" on the back I would like "TWL". Phone # 816-863-8328Name - Jeremy YiLicensed in the State of MissouriNo addressemail - dfaulk@marlowhomesexample.com

```html
<!DOCTYPE html>
<html lang="en">
<head>
<meta charset="utf-8">
<title>Marlow Realty Group – Business Card</title>
<link href="https://fonts.googleapis.com/css2?family=Archivo+Black&family=Anton&family=Lato:wght@400&display=swap" rel="stylesheet">
<style>
  :root {
    --brand-blue: #48add8;
    --card-white: #ffffff;
    --text-grey: #555a5e;
    --rule-grey: #8a8f93;
    --backdrop: #e9e6e1;
  }
  * { box-sizing: border-box; margin: 0; padding: 0; }
  html, body { width: 1200px; height: 995px; overflow: hidden; }
  body {
    background: var(--backdrop);
    display: flex;
    align-items: center;
    justify-content: center;
    gap: 120px;
  }
  .card {
    position: relative;
    width: 360px;
    height: 630px;
    border-radius: 28px;
    overflow: hidden;
    box-shadow: 0 10px 30px rgba(0,0,0,0.18);
  }

  /* Back side */
  .card-back { background: var(--brand-blue); }
  .card-back .monogram-disc {
    position: absolute;
    left: 50%;
    top: 50%;
    width: 420px;
    height: 420px;
    transform: translate(-50%, -50%);
    border-radius: 50%;
    background: var(--card-white);
    display: flex;
    align-items: center;
    justify-content: center;
  }
  .card-back .monogram {
    font-family: "Archivo Black", sans-serif;
    font-size: 118px;
    color: var(--brand-blue);
    letter-spacing: 2px;
  }

  /* Front side */
  .card-front {
    background: var(--card-white);
    display: flex;
    flex-direction: column;
    align-items: center;
  }
  .company {
    margin-top: 78px;
    font-family: "Archivo Black", sans-serif;
    color: var(--brand-blue);
    text-align: center;
    line-height: 1;
  }
  .company-name { font-size: 58px; letter-spacing: 7px; }
  .company-suffix { font-size: 29px; margin-top: 4px; letter-spacing: -0.5px; }

  .agent-name {
    margin-top: 92px;
    font-family: "Anton", sans-serif;
    font-size: 46px;
    color: var(--brand-blue);
    letter-spacing: 0.5px;
  }

  .contact {
    margin-top: 30px;
    width: 100%;
    display: flex;
    flex-direction: column;
    align-items: center;
    font-family: "Lato", sans-serif;
    color: var(--text-grey);
  }
  .contact-icon { width: 26px; height: 26px; }
  .contact-phone { font-size: 23px; letter-spacing: 1px; margin-top: 4px; }
  .contact-rule {
    width: 280px;
    height: 1px;
    background: var(--brand-blue);
    margin: 12px 0 14px;
  }
  .contact-email { font-size: 17px; margin-top: 4px; }

  .licence-band {
    position: absolute;
    left: 0;
    right: 0;
    bottom: 0;
    height: 52px;
    background: var(--brand-blue);
    border-top: 4px solid var(--card-white);
    box-shadow: 0 -2px 0 var(--rule-grey);
    display: flex;
    align-items: center;
    justify-content: center;
    font-family: "Lato", sans-serif;
    font-size: 18px;
    letter-spacing: 0.5px;
    color: var(--card-white);
  }
</style>
</head>
<body>

  <section class="card card-back" aria-label="Card back">
    <div class="monogram-disc">
      <span class="monogram">TWL</span>
    </div>
  </section>

  <section class="card card-front" aria-label="Card front">
    <div class="company">
      <div class="company-name">MARLOW</div>
      <div class="company-suffix">Realty Group, LLC.</div>
    </div>

    <div class="agent-name">DORIAN FAULK</div>

    <div class="contact">
      <svg class="contact-icon" viewBox="0 0 26 26" aria-hidden="true">
        <circle cx="13" cy="13" r="12" fill="none" stroke="var(--brand-blue)" stroke-width="2"/>
        <path d="M7 11c0-2 2-3 6-3s6 1 6 3l-2 1-1-2h-6l-1 2z" fill="var(--brand-blue)"/>
        <rect x="9" y="13" width="8" height="5" rx="1" fill="var(--brand-blue)"/>
      </svg>
      <div class="contact-phone">816-552-4917</div>
      <div class="contact-rule"></div>
      <svg class="contact-icon" viewBox="0 0 26 26" aria-hidden="true">
        <circle cx="13" cy="13" r="12" fill="none" stroke="var(--brand-blue)" stroke-width="2"/>
        <rect x="7" y="9" width="12" height="8" rx="1" fill="var(--brand-blue)"/>
        <path d="M7.5 9.5l5.5 4 5.5-4" fill="none" stroke="var(--card-white)" stroke-width="1.2"/>
      </svg>
      <div class="contact-email">dfaulk@marlowhomesexample.com</div>
    </div>

    <div class="licence-band">Licensed in the State of Missouri</div>
  </section>

</body>
</html>
```